Software product web site / landing page

We went to update our web site and landing pages

https://www.velmrino.com
https://www.tasknote7pq.com

with - mobile first design
- complementing our logo colors (blue/green)

The design should have a home/landing page and a detail page.

Style: minimalist/modern - abstract - friendly

Target Market(s)

Business with Professional Services department

Industry/Entity Type

Software

Number of Pages Required

2 page

Font styles to use
Sans Serif

Requirements
Must have
• easy to convert to html/scss for mobile + desktop
Nice to have
• apply this to web page:
• https://www.marbleframekit.com/guidelines/overview/
Should not have
• vendrafolk look

```html
<!DOCTYPE html>
<html lang="en">
<head>
<meta charset="utf-8">
<title>Velmrino – Projects + Resources</title>
<link href="https://fonts.googleapis.com/css2?family=Mulish:wght@400;600;700;800&display=swap" rel="stylesheet">
<style>
:root{
  --blue:#1461b8;
  --blue-dark:#0d4a93;
  --green:#7dc242;
  --ink:#2b2f36;
  --text:#5b616b;
  --muted:#8a9099;
  --light:#f4f7fb;
  --dark:#1c2128;
  --white:#ffffff;
}
*{margin:0;padding:0;box-sizing:border-box}
html,body{width:1200px;height:4045px;overflow:hidden}
body{font-family:"Mulish",Arial,sans-serif;color:var(--text);background:var(--white);position:relative}
.abs{position:absolute}
.btn{position:absolute;display:inline-block;background:var(--blue);color:var(--white);font-size:13px;font-weight:700;padding:8px 22px;border-radius:2px;clip-path:polygon(8% 0,100% 0,92% 100%,0 100%);z-index:2}
.section-title{font-size:30px;font-weight:800;color:var(--blue-dark)}
.section-title span{color:var(--green)}
.title-rule{display:block;width:90px;height:2px;background:var(--blue);position:relative;margin-top:10px}
.title-rule::after{content:"";position:absolute;left:-3px;top:-4px;width:10px;height:10px;border-radius:50%;background:var(--green)}
.center-rule{margin:10px auto 0}
.center-rule::after{left:40px}
p.body{font-size:12px;line-height:1.65}

/* top bar + nav */
.topbar{top:0;left:0;width:1200px;height:27px;background:var(--white);border-bottom:1px solid #e6e9ee;font-size:12px;color:var(--text);z-index:3}
.topbar .mail{left:235px;top:6px}
.topbar .phone{left:560px;top:6px}
.topbar .social{left:895px;top:7px;display:flex;gap:10px}
.topbar .social i{display:block;width:11px;height:11px;border-radius:50%;background:var(--blue)}
.nav{top:27px;left:0;width:1200px;height:42px;background:var(--white);z-index:3}
.brand{left:250px;top:8px;display:flex;align-items:center;gap:7px;font-size:22px;font-weight:800;color:var(--ink)}
.brand i{width:16px;height:16px;border-radius:50%;background:var(--blue);display:block}
.menu{left:428px;top:13px;display:flex;gap:40px;font-size:13px;color:var(--text)}
.menu .active{color:var(--blue);border-bottom:2px solid var(--green);padding-bottom:4px}
.menu svg{margin-top:1px}

/* hero */
.hero{top:69px;left:0;width:1200px;height:440px;background:linear-gradient(135deg,#e9f3fc 0%,#cfe6fa 45%,#a9d4f5 70%,#e3f1fc 100%);clip-path:polygon(0 0,100% 0,100% 82%,0 100%)}
.hero-box{left:278px;top:154px;width:350px;height:196px;border:4px solid var(--green);border-right:none}
.hero-box h1{position:absolute;left:35px;top:26px;font-size:38px;line-height:1.15;font-weight:800;color:var(--blue-dark)}
.hero-box p{position:absolute;left:35px;top:124px;width:400px;font-size:13px;line-height:1.5;color:var(--blue);font-weight:600}
.hero-down{left:582px;top:408px;width:36px;height:36px;border-radius:50%;background:var(--white);box-shadow:0 2px 8px rgba(0,0,0,.15)}
.hero-down svg{position:absolute;left:11px;top:13px}
.green-edge{left:0;width:1200px}

/* about */
.about-title{left:235px;top:560px}
.about-text{left:235px;top:636px;width:400px}
.about-img{left:655px;top:512px;width:240px;height:360px;background:linear-gradient(160deg,#f3f6fa 0%,#b9d4ec 45%,#4b85c6 75%,#e7eef6 100%)}
.partner-badge{left:840px;top:760px;width:70px;height:70px;border-radius:50%;background:#2a9ee0}
.about-btn{left:538px;top:885px}

/* services */
.services{top:944px;left:0;width:1200px;height:620px;background:linear-gradient(120deg,#2d3238 0%,#4a4f55 40%,#3a3f44 70%,#22262b 100%);clip-path:polygon(0 0,100% 8%,100% 100%,0 92%)}
.hex{position:absolute;width:150px;height:132px;clip-path:polygon(25% 0,75% 0,100% 50%,75% 100%,25% 100%,0 50%);background:var(--white);display:flex;flex-direction:column;align-items:center;justify-content:center;gap:10px;font-size:14px;font-weight:700;color:var(--blue-dark)}
.hex.active{background:var(--blue);color:var(--white)}
.hex.figure{background:linear-gradient(180deg,#eaf2fb,#b8d3ee)}
.hex .rule{width:40px;height:1px;background:var(--green)}
.svc-title{left:688px;top:1150px;font-size:26px;font-weight:700;color:var(--white)}
.svc-title span{color:var(--green)}
.svc-sub{left:688px;top:1228px;font-size:16px;font-weight:700;color:var(--green)}
.svc-text{left:688px;top:1262px;width:250px;font-size:13px;line-height:1.6;color:#e6e9ee}

/* time & expense */
.te-title{left:235px;top:1630px;font-size:19px;font-weight:800;color:var(--blue-dark)}
.te-sub{left:235px;top:1676px;font-size:13px;font-weight:700;color:var(--blue)}
.te-text{left:235px;top:1700px;width:370px;font-size:12px;line-height:1.65}
.te-frame{left:900px;top:1596px;width:62px;height:292px;background:var(--blue);clip-path:polygon(40% 8%,100% 0,100% 100%,0 100%)}
.te-video{left:634px;top:1640px;width:296px;height:222px;background:linear-gradient(180deg,#e7eef6 0%,#c9d9ea 60%,#8fa9c4 100%)}
.play{position:absolute;width:42px;height:42px;border-radius:50%;border:3px solid var(--white);background:var(--blue)}
.play::after{content:"";position:absolute;left:14px;top:10px;border-left:12px solid var(--white);border-top:8px solid transparent;border-bottom:8px solid transparent}

/* cta */
.cta{top:1942px;left:0;width:1200px;height:300px;background:linear-gradient(110deg,#3b3a3a 0%,#6b5e58 45%,#514745 70%,#2f2c2c 100%);clip-path:polygon(0 0,100% 10%,100% 100%,0 88%)}
.cta-title{position:absolute;left:0;top:2048px;width:1200px;text-align:center;font-size:28px;line-height:1.35;font-weight:700;color:var(--white)}

/* blog */
.blog-title{left:0;top:2345px;width:1200px;text-align:center}
.card{position:absolute;top:2440px;width:352px;height:392px;background:var(--white);box-shadow:0 2px 10px rgba(0,0,0,.14)}
.card .thumb{height:190px;background:linear-gradient(180deg,#1b3d6e 0%,#2d5a95 100%)}
.card.alt .thumb{background:linear-gradient(180deg,#50565e 0%,#7c838b 100%)}
.card .icons{position:absolute;right:8px;top:14px;display:flex;flex-direction:column;gap:14px}
.card .icons i{display:block;width:14px;height:14px;border-radius:50%;background:var(--green)}
.card h3{margin:16px 16px 6px;font-size:15px;color:var(--green);font-weight:700}
.card .meta{margin:0 16px;display:flex;gap:18px;font-size:10px;color:var(--muted)}
.card p{margin:10px 16px 0;font-size:11px;line-height:1.6}
.card .btn{right:14px;bottom:12px;font-size:11px;padding:6px 16px}

/* newsletter */
.news{top:2932px;left:0;width:1200px;height:365px;background:linear-gradient(120deg,#2a2c30 0%,#45474b 50%,#202226 100%);clip-path:polygon(0 8%,100% 0,100% 92%,0 100%)}
.news-kicker{left:0;top:3005px;width:1200px;text-align:center;font-size:18px;color:var(--white)}
.news-title{left:0;top:3036px;width:1200px;text-align:center;font-size:30px;font-weight:800;color:var(--white)}
.news-title span{color:var(--green)}
.news-form{left:310px;top:3132px;width:580px;height:38px;display:flex}
.news-form .field{flex:1;background:var(--white);font-size:13px;color:var(--muted);padding:11px 16px;clip-path:polygon(3% 0,100% 0,100% 100%,0 100%)}
.news-form .submit{width:130px;background:var(--blue);color:var(--white);font-size:15px;font-weight:700;text-align:center;padding-top:9px;clip-path:polygon(0 0,100% 0,90% 100%,0 100%)}

/* testimonial */
.testi-title{left:0;top:3328px;width:1200px;text-align:center}
.avatar{left:572px;top:3398px;width:56px;height:56px;border-radius:50%;background:linear-gradient(180deg,#8d8d8d,#4a4a4a);border:2px solid #ddd}
.testi-name{left:0;top:3465px;width:1200px;text-align:center;font-size:13px;color:var(--ink);font-weight:600}
.testi-text{left:380px;top:3490px;width:440px;text-align:center;font-size:12px;line-height:1.6;z-index:1}
.quote{font-size:180px;line-height:1;color:#e3e6ea;font-weight:800;font-family:Georgia,serif}
.arrow{width:26px;height:26px;border-radius:50%;background:#e6e9ee}
.arrow svg{position:absolute;left:8px;top:7px}

/* footer */
.footer{top:3690px;left:0;width:1200px;height:355px;background:#181b20;clip-path:polygon(0 8%,100% 0,100% 100%,0 100%)}
.foot-h{top:3780px;font-size:18px;font-weight:700;color:var(--green)}
.foot-rule{top:3810px;width:110px;height:1px;background:#3b4048}
.foot-links{left:235px;top:3826px;font-size:12px;line-height:2.05;color:#c8ccd2}
.foot-links li{list-style:none}
.foot-links li:first-child{color:var(--green)}
.contact{left:445px;top:3826px;font-size:12px;line-height:1.6;color:#c8ccd2}
.contact div{display:flex;gap:8px;margin-bottom:14px}
.contact svg{flex:none;margin-top:2px}
.foot-social{left:450px;top:3965px;display:flex;gap:22px}
.foot-social i{display:block;width:10px;height:10px;border-radius:2px;background:#c8ccd2}
.newsitem{left:707px;display:flex;gap:10px;width:240px}
.newsitem .pic{width:46px;height:46px;flex:none;background:linear-gradient(160deg,#dfe9f3,#8fb2d6)}
.newsitem p{font-size:12px;color:var(--white);line-height:1.4}
.newsitem small{display:block;font-size:10px;color:var(--muted);margin-top:4px}
.copyright{left:0;top:4022px;width:1200px;text-align:center;font-size:11px;color:var(--muted)}
</style>
</head>
<body>

<!-- top bar -->
<div class="abs topbar">
  <span class="abs mail">info@velmrino.com</span>
  <span class="abs phone">+1 (555) 014-2937</span>
  <div class="abs social"><i></i><i></i><i></i><i></i></div>
</div>
<nav class="abs nav">
  <div class="abs brand"><i></i>Velmrino</div>
  <div class="abs menu">
    <span class="active">Home</span><span>About Us</span><span>Features</span><span>Products</span><span>Solutions</span><span>Blog</span><span>Contact Us</span>
    <svg width="12" height="12" viewBox="0 0 12 12"><circle cx="5" cy="5" r="4" fill="none" stroke="#5b616b" stroke-width="1.5"/><path d="M8 8l3 3" stroke="#5b616b" stroke-width="1.5"/></svg>
  </div>
</nav>

<!-- hero -->
<div class="abs hero" role="img" aria-label="Abstract pattern of translucent blue rounded squares"></div>
<svg class="abs green-edge" style="top:420px" width="1200" height="100" viewBox="0 0 1200 100"><polygon points="0,89 1200,10 1200,22 0,100" fill="#7dc242"/></svg>
<div class="abs hero-box">
  <h1>Projects +<br>Resources</h1>
  <p>Create Projects from Templates Or Opportunities - Allocate<br>Resources To Tasks - Track Progress</p>
</div>
<div class="abs hero-down"><svg width="14" height="10" viewBox="0 0 14 10"><path d="M1 1l6 6 6-6" fill="none" stroke="#1461b8" stroke-width="2"/></svg></div>

<!-- about -->
<div class="abs about-title"><h2 class="section-title">Some Words <span>About Us</span></h2><span class="title-rule"></span></div>
<p class="abs body about-text">Velmrino is different – unlike other PSA software, Velmrino is available as a native Nimbusforce application, giving you the versatility to customize objects and extend this application within Nimbusforce with a minimal learning curve. All data is securely stored in Nimbusforce and with that available for all reporting and dashboard options.<br>In addition to our personalized product support, we provide customization and configuration services, training and an expert Help Desk. Velmrino is a truly professional services automation – for professionals. Get a free Demo and experience for yourself the smarter, easier, more powerful PSA solution. Velmrino includes consulting businesses and departments, art agencies and service delivery companies of all sizes among its satisfied customers.</p>
<div class="abs about-img" role="img" aria-label="Business handshake in front of a city skyline"></div>
<div class="abs partner-badge" role="img" aria-label="Partner badge"></div>
<span class="btn about-btn">Read More</span>

<!-- services -->
<div class="abs services" role="img" aria-label="Team working at computers in a dim office"></div>
<svg class="abs green-edge" style="top:930px" width="1200" height="80" viewBox="0 0 1200 80"><polygon points="0,14 1200,62 1200,74 0,24" fill="#7dc242"/></svg>
<svg class="abs green-edge" style="top:1480px" width="1200" height="100" viewBox="0 0 1200 100"><polygon points="0,30 1200,80 1200,92 0,40" fill="#7dc242"/></svg>
<div class="hex active" style="left:365px;top:1034px">
  <svg width="30" height="26" viewBox="0 0 30 26"><rect x="2" y="6" width="26" height="18" rx="2" fill="none" stroke="#fff" stroke-width="2"/><path d="M10 6V2h10v4" fill="none" stroke="#fff" stroke-width="2"/></svg>
  Projects<span class="rule"></span></div>
<div class="hex" style="left:230px;top:1107px">
  <svg width="28" height="28" viewBox="0 0 28 28"><circle cx="14" cy="15" r="10" fill="none" stroke="#1461b8" stroke-width="2"/><path d="M14 9v6l4 3M4 4l20 20" stroke="#1461b8" stroke-width="2" fill="none"/></svg>
  Time-off<span class="rule"></span></div>
<div class="hex" style="left:500px;top:1107px">
  <svg width="28" height="28" viewBox="0 0 28 28"><circle cx="14" cy="14" r="11" fill="none" stroke="#1461b8" stroke-width="2"/><path d="M14 7v7l5 4" stroke="#1461b8" stroke-width="2" fill="none"/></svg>
  Time<span class="rule"></span></div>
<div class="hex figure" style="left:365px;top:1202px" role="img" aria-label="Illustration of a consultant at a laptop"></div>
<div class="hex" style="left:230px;top:1264px">
  <svg width="26" height="30" viewBox="0 0 26 30"><path d="M3 2h20v26l-4-3-3 3-3-3-3 3-3-3-4 3z" fill="none" stroke="#1461b8" stroke-width="2"/><path d="M8 10h10M8 16h10" stroke="#1461b8" stroke-width="2"/></svg>
  Billing<span class="rule"></span></div>
<div class="hex" style="left:500px;top:1264px">
  <svg width="30" height="24" viewBox="0 0 30 24"><rect x="2" y="4" width="26" height="16" rx="2" fill="none" stroke="#1461b8" stroke-width="2"/><path d="M2 9h26" stroke="#1461b8" stroke-width="3"/></svg>
  Expenses<span class="rule"></span></div>
<div class="hex" style="left:365px;top:1336px">
  <svg width="32" height="26" viewBox="0 0 32 26"><circle cx="16" cy="8" r="5" fill="none" stroke="#1461b8" stroke-width="2"/><path d="M6 24c0-6 4-9 10-9s10 3 10 9" fill="none" stroke="#1461b8" stroke-width="2"/></svg>
  Resources<span class="rule"></span></div>
<div class="abs svc-title">Our <span>Services</span><span class="title-rule" style="margin-top:8px"></span></div>
<div class="abs svc-sub">Projects</div>
<p class="abs svc-text">Assign Time to Projects. Projects can be created from Opportunities or from a template</p>

<!-- time & expense -->
<div class="abs te-title">Time and Expense Management<span class="title-rule" style="margin-top:8px"></span></div>
<div class="abs te-sub">Integrating project and resource management with billing.</div>
<p class="abs te-text">Velmrino is professional-grade time and expense management software that gives you the power to seamlessly go beyond project and resource management with billing – from opportunity to project to invoice and payroll integration. Streamline processes, improve efficiencies and sharpen profit visibility with Velmrino's advanced metrics, flexible functionality and user-friendly interface.</p>
<span class="btn" style="left:494px;top:1835px">Demo</span>
<div class="abs te-frame"></div>
<div class="abs te-video" role="img" aria-label="Illustration of a manager thinking about time and expenses"><span class="play" style="left:-21px;top:90px"></span></div>

<!-- cta -->
<div class="abs cta" role="img" aria-label="Colleagues discussing work around a whiteboard"></div>
<svg class="abs green-edge" style="top:2160px" width="1200" height="100" viewBox="0 0 1200 100"><polygon points="0,42 1200,78 1200,90 0,54" fill="#7dc242"/></svg>
<h2 class="cta-title">See Time+expenses Demo Work<br>In Your Organization</h2>
<span class="btn" style="left:497px;top:2160px;font-size:15px;padding:10px 34px">Schedule A Demo</span>

<!-- blog -->
<div class="abs blog-title"><h2 class="section-title">Our <span>Blog</span></h2><span class="title-rule center-rule"></span></div>
<article class="card" style="left:243px">
  <div class="thumb" role="img" aria-label="Screenshot of mobile time entry"></div>
  <span class="play" style="left:155px;top:74px"></span>
  <div class="icons"><i></i><i></i><i></i><i></i></div>
  <h3>Enter Time – Mobile</h3>
  <div class="meta"><span>Emily Smith</span><span>28 September</span><span>No Comments</span></div>
  <p>Enter time on mobile If you are on the go, you can capture time directly from your mobile device or browser on the Velmrino tab; click on Home or go directly to the app, log in with your Nimbusforce credentials, enter time on a convenient form in just 30 to 90 minutes or 1.30...</p>
  <span class="btn">Read More</span>
</article>
<article class="card alt" style="left:612px">
  <div class="thumb" role="img" aria-label="Screenshot of capturing time from a case"></div>
  <span class="play" style="left:155px;top:74px"></span>
  <div class="icons"><i></i><i></i><i></i><i></i></div>
  <h3>Capture Time from Case – Demo</h3>
  <div class="meta"><span>Emily Smith</span><span>28 September</span><span>No Comments</span></div>
  <p>Capture time from case In addition to entering the time in the timesheet, you can capture time directly from any Nimbusforce object you spend time on. Let's use cases as an example; go to the Nimbusforce Cases tab, pick a case and click Capture Time button, enter time spent you will...</p>
  <span class="btn">Read More</span>
</article>
<span class="btn" style="left:555px;top:2872px">View All</span>

<!-- newsletter -->
<div class="abs news" role="img" aria-label="Close-up of a business handshake"></div>
<svg class="abs green-edge" style="top:2920px" width="1200" height="60" viewBox="0 0 1200 60"><polygon points="0,30 1200,0 1200,10 0,40" fill="#7dc242"/></svg>
<svg class="abs green-edge" style="top:3250px" width="1200" height="60" viewBox="0 0 1200 60"><polygon points="0,40 1200,10 1200,20 0,50" fill="#7dc242"/></svg>
<div class="abs news-kicker">Join Our Mail List</div>
<div class="abs news-title">Subscribe Our <span>Newsletter</span></div>
<div class="abs news-form"><span class="field">Enter Your Email Address</span><span class="submit">Subscribe</span></div>

<!-- testimonial -->
<div class="abs testi-title"><h2 class="section-title">Our <span>Testimonial</span></h2><span class="title-rule center-rule"></span></div>
<div class="abs avatar" role="img" aria-label="Customer portrait"></div>
<div class="abs testi-name">Jhon Deo</div>
<span class="abs quote" style="left:275px;top:3440px">“</span>
<span class="abs quote" style="left:840px;top:3440px">”</span>
<div class="abs arrow" style="left:240px;top:3520px"><svg width="10" height="12" viewBox="0 0 10 12"><path d="M8 1L2 6l6 5" fill="none" stroke="#8a9099" stroke-width="2"/></svg></div>
<div class="abs arrow" style="left:935px;top:3520px"><svg width="10" height="12" viewBox="0 0 10 12"><path d="M2 1l6 5-6 5" fill="none" stroke="#8a9099" stroke-width="2"/></svg></div>
<p class="abs testi-text">Lorem Ipsum is simply dummy text of the printing and typesetting industry. Lorem Ipsum has been the industry's standard dummy text ever since the 1500s, when an unknown printer took a galley of type and scrambled it to make a type specimen book. It has survived not only five centuries, but also the leap into electronic typesetting, remaining essentially unchanged.</p>
<span class="btn" style="left:553px;top:3638px">Read More</span>

<!-- footer -->
<div class="abs footer"></div>
<svg class="abs green-edge" style="top:3680px" width="1200" height="40" viewBox="0 0 1200 40"><polygon points="0,36 1200,6 1200,12 0,42" fill="#7dc242"/></svg>
<div class="abs foot-h" style="left:235px">Quick Links</div><div class="abs foot-rule" style="left:235px"></div>
<div class="abs foot-h" style="left:445px">Contact Us</div><div class="abs foot-rule" style="left:445px"></div>
<div class="abs foot-h" style="left:707px">Latest News</div><div class="abs foot-rule" style="left:707px"></div>
<ul class="abs foot-links"><li>Demo</li><li>Support</li><li>Documentation</li><li>Privacy</li><li>Terms</li><li>Contact</li></ul>
<div class="abs contact">
  <div><svg width="12" height="10" viewBox="0 0 12 10"><rect x="0.5" y="0.5" width="11" height="9" fill="none" stroke="#c8ccd2"/><path d="M1 1l5 4 5-4" fill="none" stroke="#c8ccd2"/></svg>info@velmrino.com</div>
  <div><svg width="12" height="12" viewBox="0 0 12 12"><path d="M2 1l3 0 1 3-2 1c1 2 2 3 4 4l1-2 3 1v3c-6 0-10-4-10-10z" fill="#c8ccd2"/></svg>+1 (555) 014-2937</div>
  <div><svg width="10" height="13" viewBox="0 0 10 13"><path d="M5 12C2 8 1 6 1 4.5a4 4 0 018 0C9 6 8 8 5 12z" fill="none" stroke="#c8ccd2"/><circle cx="5" cy="4.5" r="1.4" fill="#c8ccd2"/></svg>18 Larkmoor Plaza # 214<br>Fenwick City, CA 94000</div>
</div>
<div class="abs foot-social"><i></i><i></i><i></i><i></i></div>
<div class="abs newsitem" style="top:3826px"><span class="pic" role="img" aria-label="News thumbnail"></span><p>Lorem Ipsum is simply dummy text of the printing...<small>March 26, 2018</small></p></div>
<div class="abs newsitem" style="top:3900px"><span class="pic" role="img" aria-label="News thumbnail"></span><p>Lorem Ipsum is simply dummy text of the printing...<small>March 26, 2018</small></p></div>
<div class="abs copyright">Copyright © Velmrino 2018-2019</div>

</body>
</html>
```